CoveysArmsPersonal

I am a cutting edge, top of the line gun store. We are expanding faster than we can keep up. We offer: Gunsmithing, Transfers, Concealed Carry, Machine Guns, Suppressors. My colors are reflected in my logo. Red, black and white. I like a clean design that gets the point across. I was trying to find a plastic business card, but will settle with a high quality paper product.

Contact Information for Business Card

Dwayne Covey - Owner
620-514-8826 (Cell)
Covey's Range Outfitters
1847 E. Hwy 9
Healy, KS 67462
sales@coveysrangeoutfitters.com
coveysrangeoutfitters.com

```html
<!DOCTYPE html>
<html lang="en">
<head>
<meta charset="utf-8">
<title>Covey's Range Outfitters – Business Card</title>
<link rel="stylesheet" href="https://fonts.googleapis.com/css2?family=Exo+2:wght@400;600;700&display=swap">
<style>
  :root {
    --brand-red: #7a0c0c;
    --ink: #111111;
    --paper: #ffffff;
    --backdrop: #e9e7e4;
  }
  * { box-sizing: border-box; margin: 0; padding: 0; }
  html, body { width: 1200px; height: 1033px; overflow: hidden; }
  body {
    background: var(--backdrop);
    font-family: "Exo 2", sans-serif;
    color: var(--ink);
    position: relative;
  }
  .card {
    position: absolute;
    left: 250px;
    width: 700px;
    height: 400px;
    background: var(--paper);
    box-shadow: 0 6px 20px rgba(0,0,0,0.18);
    overflow: hidden;
  }
  .card--front { top: 50px; }
  .card--back { top: 560px; }

  /* Brand lockup */
  .brand { position: absolute; display: flex; align-items: center; }
  .brand__dot { border-radius: 50%; background: var(--brand-red); flex: none; }
  .brand__name { font-weight: 700; color: var(--ink); white-space: nowrap; }
  .card--front .brand { left: 0; right: 0; top: 150px; flex-direction: column; gap: 14px; }
  .card--front .brand__dot { width: 60px; height: 60px; }
  .card--front .brand__name { font-size: 36px; line-height: 40px; }
  .card--back .brand { left: 36px; top: 34px; width: 250px; flex-direction: column; gap: 10px; }
  .card--back .brand__dot { width: 46px; height: 46px; }
  .card--back .brand__name { font-size: 21px; line-height: 24px; }

  /* Social list */
  .social { position: absolute; right: 0; top: 44px; width: 340px; list-style: none; }
  .social__item {
    display: flex; align-items: center; justify-content: flex-end;
    height: 36px; margin-bottom: 17px;
    color: var(--brand-red); font-size: 18px; white-space: nowrap;
  }
  .social__dot { width: 36px; height: 36px; border-radius: 50%; background: var(--brand-red); margin-left: 14px; flex: none; }
  .social__line { width: 40px; height: 3px; background: var(--brand-red); flex: none; }

  /* Name band */
  .name-band { position: absolute; left: 0; top: 206px; width: 700px; height: 50px; }
  .name-band__graphic { position: absolute; inset: 0; }
  .name-band__graphic polygon, .name-band__graphic rect { fill: var(--ink); }
  .holder { position: absolute; left: 14px; top: 4px; color: var(--paper); }
  .holder__name { font-size: 19px; font-weight: 600; line-height: 20px; letter-spacing: 0.5px; }
  .holder__role { font-size: 12px; line-height: 14px; }

  /* Contact details */
  .contact { position: absolute; list-style: none; font-size: 18px; color: var(--brand-red); }
  .contact--left { left: 20px; top: 276px; }
  .contact--right { left: 356px; top: 318px; }
  .contact__item { display: flex; align-items: flex-start; gap: 10px; line-height: 24px; margin-bottom: 8px; white-space: nowrap; }
  .contact__icon { width: 20px; height: 20px; margin-top: 2px; flex: none; }
  .contact__icon circle { fill: var(--brand-red); }
  .contact__icon path, .contact__icon rect { fill: var(--paper); }
  .contact__icon .stroke { fill: none; stroke: var(--paper); stroke-width: 1.4; }
</style>
</head>
<body>

<section class="card card--front" aria-label="Card front">
  <div class="brand">
    <span class="brand__dot"></span>
    <span class="brand__name">Covey's Range Outfitters</span>
  </div>
</section>

<section class="card card--back" aria-label="Card back">
  <div class="brand">
    <span class="brand__dot"></span>
    <span class="brand__name">Covey's Range Outfitters</span>
  </div>

  <ul class="social">
    <li class="social__item">socialpage.com/urname<span class="social__dot"></span><span class="social__line"></span></li>
    <li class="social__item">@yourhandle<span class="social__dot"></span><span class="social__line"></span></li>
    <li class="social__item">Video Chat<span class="social__dot"></span><span class="social__line"></span></li>
  </ul>

  <div class="name-band">
    <svg class="name-band__graphic" width="700" height="50" viewBox="0 0 700 50">
      <polygon points="0,0 195,0 214,40 0,40"/>
      <polygon points="224,0 242,0 262,40 244,40"/>
      <polygon points="256,0 274,0 294,40 276,40"/>
      <polygon points="288,0 306,0 326,40 308,40"/>
      <polygon points="320,0 338,0 358,40 340,40"/>
      <rect x="0" y="40" width="676" height="8"/>
    </svg>
    <div class="holder">
      <p class="holder__name">DWAYNE COVEY</p>
      <p class="holder__role">Owner</p>
    </div>
  </div>

  <ul class="contact contact--left">
    <li class="contact__item">
      <svg class="contact__icon" viewBox="0 0 20 20"><circle cx="10" cy="10" r="10"/><path d="M6.5 5.2c.6-.4 1.3-.3 1.6.3l.8 1.5c.3.5.1 1.1-.3 1.4l-.5.3c.5 1.2 1.4 2.1 2.6 2.6l.3-.5c.3-.4.9-.6 1.4-.3l1.5.8c.6.3.7 1 .3 1.6-.7 1-1.9 1.4-3 .9-2.4-1-4.2-2.8-5.2-5.2-.4-1.1 0-2.3.5-3.4z"/></svg>
      <span>620-514-8826</span>
    </li>
    <li class="contact__item">
      <svg class="contact__icon" viewBox="0 0 20 20"><circle cx="10" cy="10" r="10"/><rect x="7" y="4.5" width="6" height="11" rx="1.2"/><rect x="9" y="13" width="2" height="1.2" style="fill:var(--brand-red)"/></svg>
      <span>620-514-8826 (Cell)</span>
    </li>
    <li class="contact__item">
      <svg class="contact__icon" viewBox="0 0 20 20"><circle cx="10" cy="10" r="10"/><path d="M10 4a4 4 0 0 1 4 4c0 2.8-4 7.5-4 7.5S6 10.8 6 8a4 4 0 0 1 4-4zm0 2.4a1.6 1.6 0 1 0 0 3.2 1.6 1.6 0 0 0 0-3.2z"/></svg>
      <span>1847 E. Hwy 9<br>Healy, KS 67462</span>
    </li>
  </ul>

  <ul class="contact contact--right">
    <li class="contact__item">
      <svg class="contact__icon" viewBox="0 0 20 20"><circle cx="10" cy="10" r="10"/><rect x="5" y="6.5" width="10" height="7" rx="1"/><path class="stroke" d="M5.5 7l4.5 3.5L14.5 7" style="stroke:var(--brand-red)"/></svg>
      <span>sales@coveysrangeoutfitters.com</span>
    </li>
    <li class="contact__item">
      <svg class="contact__icon" viewBox="0 0 20 20"><circle cx="10" cy="10" r="10"/><circle class="stroke" cx="10" cy="10" r="5.5" style="fill:none"/><path class="stroke" d="M4.5 10h11M10 4.5c-2.2 2.8-2.2 8.2 0 11M10 4.5c2.2 2.8 2.2 8.2 0 11"/></svg>
      <span>coveysrangeoutfitters.com</span>
    </li>
  </ul>
</section>

</body>
</html>
```